Website Needs a New Look & Feel - I am Too Old and Uncool on my Own

I want some design ideas for my current site. I need a new, more modern and dynamic look and feel. The audience for the site is 90% male, 24-54 years old, and not highly educated. English is second language for about 30% of audience, so images help. 85% of visitors view on mobile. We sell trucks and trailers to this audience. . Just want something new and cool. Tired of what I have. Current site doesn't seem strong enough to match the kind of people who drive trucks for a living. Current is site is brelvon.com. Pull relevant menu and text from the site.

Target Market(s)

Truck Drivers and Trucking Company Owners (90% male).

Industry/Entity Type

Transportation - Specifically, truck and trailer sales.

Number of Pages Required

3 page

Font styles to use
Sans Serif

Colors
0054AA
0677BA
7BADD7
CADEEF
E8F1F8

Requirements
Must have
• Images of Sleeper Trucks (like on there now) and trailers. Audience is very literal, so they need to see what we sell.
Nice to have
• Images of Sleeper Trucks (like on tMy inventory pages are boring, please show me something more user-friendly and interesting. here now) and trailers.

```html
<!DOCTYPE html>
<html lang="en">
<head>
<meta charset="utf-8">
<title>Brelvon Truck &amp; Trailer</title>
<link href="https://fonts.googleapis.com/css2?family=Plus+Jakarta+Sans:wght@400;500;600;700&family=Oswald:wght@500&display=swap" rel="stylesheet">
<style>
:root{
  --ink:#111418;
  --muted:#5a6470;
  --blue:#0677BA;
  --blue-deep:#0054AA;
  --blue-mid:#7BADD7;
  --blue-soft:#CADEEF;
  --blue-pale:#E8F1F8;
  --card:#EEF3F8;
  --footer:#F2F5F8;
  --white:#ffffff;
}
*{margin:0;padding:0;box-sizing:border-box}
html,body{width:1200px;height:4570px;overflow:hidden}
body{position:relative;font-family:"Plus Jakarta Sans",sans-serif;color:var(--ink);background:var(--white)}
.abs{position:absolute}
.btn{position:absolute;display:flex;align-items:center;justify-content:center;background:var(--blue);color:var(--white);border-radius:40px;font-weight:700;font-size:14px}
.btn-outline{position:absolute;display:flex;align-items:center;justify-content:center;border:1.5px solid var(--ink);border-radius:40px;font-weight:700;font-size:13px;width:100px;height:36px}
.eyebrow{position:absolute;font-size:15px;font-weight:500;padding-left:10px;border-left:4px solid var(--blue);line-height:16px}
.h2{position:absolute;font-size:48px;font-weight:500;line-height:1.05;letter-spacing:-0.5px}
.para{position:absolute;font-size:13.5px;line-height:21px;color:var(--muted)}
.photo{position:absolute}

/* header */
.logo-name{font-weight:700;color:var(--ink);line-height:1}
.nav{position:absolute;left:382px;top:48px;display:flex;gap:21px;font-size:13.5px;font-weight:600}

/* hero */
.hero-bg{left:0;top:0;width:1200px;height:810px;background:linear-gradient(180deg,#e9f0f9 0%,#f1f5fa 30%,#dfe6ee 55%,#aebccb 80%,#8fa0b2 100%)}
.hero-photo{left:0;top:300px;width:1200px;height:510px;background:linear-gradient(90deg,#c8d2dc 0%,#e7ebef 30%,#9bb4cf 60%,#3f78b8 78%,#2a5f9c 100%);opacity:.85}
.hero-title{left:170px;top:190px;font-size:64px;font-weight:500;line-height:62px;letter-spacing:-0.5px}
.hero-title .accent{color:var(--blue)}
.hero-sub{left:170px;top:322px;font-size:27px;font-weight:500;padding-left:12px;border-left:5px solid var(--blue);line-height:28px}

/* fit cards */
.fit-card{position:absolute;top:966px;width:343px;height:374px;background:var(--card);border-radius:8px}
.fit-card h3{position:absolute;left:30px;top:28px;font-size:27px;font-weight:500}
.fit-card .photo{left:30px;top:78px;width:283px;height:200px;background:linear-gradient(180deg,var(--card),#d7dde4 45%,#b9c2cc 80%,var(--card));border-radius:4px}
.fit-card p{position:absolute;left:30px;top:290px;width:283px;font-size:12.5px;line-height:20px;color:var(--muted)}
.counter{position:absolute;left:896px;top:898px;display:flex;align-items:center;gap:6px;color:var(--blue)}
.counter .num{font-family:"Oswald",sans-serif;font-size:40px;line-height:1}
.counter .total{font-family:"Oswald",sans-serif;font-size:22px;color:var(--muted);line-height:1;margin-top:12px}

/* wholesale */
.wholesale-bg{left:0;top:1395px;width:1200px;height:555px;background:linear-gradient(180deg,#fff 0%,#eef2f6 35%,#e2e8ee 100%)}
.circle{position:absolute;border-radius:50%}

/* inventory */
.inv-img{position:absolute;top:2094px;width:270px;height:222px;border-radius:5px;background:linear-gradient(180deg,#8bb4e0 0%,#dce3ea 50%,#9ea6ad 100%)}
.inv-meta{position:absolute;top:2330px;width:270px}
.inv-meta .cat{font-size:11.5px;color:var(--muted);text-transform:uppercase}
.inv-meta h4{font-size:16px;font-weight:500;line-height:21px;margin-top:2px}
.inv-price{position:absolute;top:2407px;font-size:13.5px;color:var(--muted)}

/* buying */
.buy-bg{left:0;top:2485px;width:1200px;height:803px;background:#f7f9fb}
.ticks{position:absolute;left:607px;top:3078px;width:420px;list-style:none}
.ticks li{position:relative;padding-left:20px;font-size:13px;line-height:20px;color:var(--muted);margin-bottom:23px}
.ticks svg{position:absolute;left:0;top:3px}

/* blog */
.blog-img{position:absolute;top:3500px;width:270px;height:254px;border-radius:5px}
.blog-meta{position:absolute;top:3766px;width:270px}
.blog-meta .date{font-size:11.5px;color:var(--muted)}
.blog-meta h4{font-size:19px;font-weight:600;line-height:23px;margin-top:6px}
.blog-meta p{font-size:13px;line-height:21px;color:var(--muted);margin-top:8px}

/* cta */
.cta-bg{left:0;top:3935px;width:1200px;height:368px;background:linear-gradient(90deg,#2c4d7a 0%,#1f5bb8 28%,#3f5168 55%,#25303c 100%)}

/* footer */
.footer-bg{left:0;top:4303px;width:1200px;height:267px;background:var(--footer)}
.foot-col{position:absolute;top:4352px}
.foot-col h5{font-size:16px;font-weight:600;margin-bottom:8px}
.foot-col a{display:block;font-size:13px;line-height:21px;color:var(--muted);text-decoration:none}
.social{position:absolute;top:4437px;width:36px;height:36px;border:1.5px solid var(--ink);border-radius:50%}
.legal{position:absolute;top:4541px;font-size:13px;color:var(--muted)}
</style>
</head>
<body>

<!-- HERO -->
<section class="hero">
  <div class="abs hero-bg"></div>
  <div class="photo hero-photo" role="img" aria-label="Row of parked sleeper trucks led by a blue semi truck under a clear sky"></div>
  <div class="abs" style="left:170px;top:32px">
    <div class="logo-name" style="font-size:34px;letter-spacing:1px">BRELVON</div>
    <div class="logo-name" style="font-size:19px;margin-top:2px">Truck &amp; Trailer</div>
  </div>
  <nav class="nav"><span>Sleepers</span><span>Reefers</span><span>Dry Vans</span><span>Cranes</span><span>Resources</span><span>Contact</span></nav>
  <a class="btn" style="left:864px;top:37px;width:160px;height:43px">See Our Inventory</a>
  <h1 class="abs hero-title">Buy Like <span class="accent">a Fleet</span><br>Save Thousands</h1>
  <p class="abs hero-sub">This is no Evolution, it’s a Revolution</p>
</section>

<!-- RIGHT FIT -->
<section class="fit">
  <div class="eyebrow" style="left:170px;top:862px">Experience a Suite Of Improvements</div>
  <h2 class="h2" style="left:168px;top:884px">Find The Right Fit</h2>
  <div class="counter">
    <svg width="26" height="12" viewBox="0 0 26 12"><path d="M25 6H2M7 1 2 6l5 5" fill="none" stroke="#111418" stroke-width="1.6"/></svg>
    <span class="num">01</span><span style="font-size:34px;color:var(--blue-mid);font-family:Oswald,sans-serif">/</span><span class="total">04</span>
    <svg width="26" height="12" viewBox="0 0 26 12"><path d="M1 6h23M19 1l5 5-5 5" fill="none" stroke="#111418" stroke-width="1.6"/></svg>
  </div>

  <article class="fit-card" style="left:170px">
    <h3>Reefer Trailers</h3>
    <div class="photo" role="img" aria-label="White refrigerated trailer with front cooling unit"></div>
    <p>Ranging typically from 48 to 53 feet in length, these trailers use diesel-powered units to maintain consistent, precise temperatures.</p>
  </article>
  <article class="fit-card" style="left:536px">
    <h3>Sleepers</h3>
    <div class="photo" role="img" aria-label="White sleeper cab semi truck"></div>
    <p>Whether you’re an owner, operator or outfit a fleet, these rugged sleepers combine legendary builds from trusted brands</p>
  </article>
  <article class="fit-card" style="left:903px">
    <h3>Dry Vans</h3>
    <div class="photo" role="img" aria-label="White dry van trailer"></div>
    <p>Ranging typically from 48 to 53 feet in length, these trailers use diesel-powered units to maintain consistent, precise temperatures.</p>
  </article>
  <div class="abs" style="left:170px;top:1370px;width:1030px;height:1px;background:var(--blue-soft)"></div>
  <div class="abs" style="left:170px;top:1369px;width:343px;height:4px;background:var(--ink)"></div>
</section>

<!-- WHOLESALE -->
<section class="wholesale">
  <div class="abs wholesale-bg" role="img" aria-label="Soft misty landscape with a road fading into the distance"></div>
  <div class="circle" role="img" aria-label="Refrigerated trailers parked on a lot under blue sky" style="left:179px;top:1427px;width:466px;height:466px;background:linear-gradient(160deg,#3f86cf 0%,#8cb6e2 30%,#e6eaee 55%,#9aa3ac 85%,#6e767e 100%)"></div>
  <div class="circle" role="img" aria-label="Row of colourful semi trucks at a dealership" style="left:506px;top:1617px;width:196px;height:196px;border:5px solid #fff;background:linear-gradient(180deg,#6aa2dc 0%,#c4d4e4 45%,#a33d3f 70%,#7c858e 100%)"></div>
  <div class="eyebrow" style="left:731px;top:1462px">Step Into Your New Office</div>
  <h2 class="h2" style="left:731px;top:1484px;line-height:50px">Wholesale<br>Reefers,<br>Dry Vans and<br>Sleepers</h2>
  <p class="para" style="left:731px;top:1700px;width:300px">Brelvon Truck &amp; Trailer is an equipment dealership in Kansas City, offering wholesale reefers, dry vans, and sleepers at the best prices. We aren’t a normal dealership, because you can buy directly from us at wholesale price and save thousands. We don’t have a fancy sales lot, but we do have the lowest prices on good, clean equipment in the country.</p>
</section>

<!-- INVENTORY -->
<section class="inventory">
  <div class="eyebrow" style="left:170px;top:1998px">Our Trucks and Trailers</div>
  <h2 class="h2" style="left:168px;top:2020px">Efficient Transportation</h2>
  <a class="btn" style="left:841px;top:2018px;width:183px;height:44px">See Our Inventory</a>

  <div class="inv-img" style="left:170px" role="img" aria-label="White sleeper truck parked on a dirt lot"></div>
  <div class="inv-meta" style="left:170px"><div class="cat">Sleeper</div><h4>2020 HAULMARK Ridgeline<br>319,417 Miles</h4></div>
  <div class="inv-price" style="left:170px">Price: $63,000</div>
  <a class="btn-outline" style="left:339px;top:2396px">See Details</a>

  <div class="inv-img" style="left:463px" role="img" aria-label="Reefer trailers with front cooling units lined up"></div>
  <div class="inv-meta" style="left:463px"><div class="cat">Reefers</div><h4>2025 Frostline S-600 or S-700<br>Reefers on 2019 Unitrail Trailers</h4></div>
  <div class="inv-price" style="left:463px">Price: $63,000</div>
  <a class="btn-outline" style="left:632px;top:2396px">See Details</a>

  <div class="inv-img" style="left:756px;background:linear-gradient(180deg,#b9cde0 0%,#e4e8ec 45%,#a4acb4 100%)" role="img" aria-label="Side view of silver dry van trailer"></div>
  <div class="inv-meta" style="left:756px"><div class="cat">Dry Vans</div><h4>2014-2019 Greyhaven &amp; Unitrail -<br>60 Units Available</h4></div>
  <div class="inv-price" style="left:756px">Price: $17,000</div>
  <a class="btn-outline" style="left:925px;top:2396px">See Details</a>
</section>

<!-- BUYING -->
<section class="buying">
  <div class="abs buy-bg"></div>
  <div class="eyebrow" style="left:170px;top:2536px">Designed to Change Everything</div>
  <h2 class="h2" style="left:170px;top:2557px;line-height:53px">Buying From<br>Brelvon Truck and<br>Trailer</h2>
  <p class="abs" style="left:170px;top:2727px;font-size:13px;color:var(--muted)">When you buy from Brelvon, you are buying at a “wholesale price.”</p>
  <div class="photo" role="img" aria-label="Grey sleeper truck parked beside a red truck under tall trees" style="left:170px;top:2764px;width:416px;height:470px;border-radius:14px;background:linear-gradient(180deg,#3f7fd0 0%,#9cbbe0 35%,#4d5866 65%,#8a8f88 100%)"></div>
  <div class="circle" role="img" aria-label="Truck hauling a white trailer on a highway" style="left:609px;top:2535px;width:344px;height:344px;background:linear-gradient(180deg,#7aa0c8 0%,#5f8a4a 35%,#a9acaa 60%,#6a8a50 100%)"></div>
  <div class="circle" style="left:920px;top:2677px;width:106px;height:106px;background:var(--blue);display:flex;align-items:center;justify-content:center;gap:6px;color:#fff;font-weight:700;font-size:14px">
    <svg width="12" height="14" viewBox="0 0 12 14"><path d="M1 1l10 6-10 6z" fill="#fff"/></svg>Play
  </div>
  <h3 class="abs" style="left:606px;top:2904px;font-size:28px;font-weight:500">How Are The Prices So Low?</h3>
  <p class="para" style="left:607px;top:2950px;width:425px;font-size:13px">As one of the leading equipment dealerships in the U.S., Brelvon Truck &amp; Trailer is committed to going the extra mile. We believe that offering the best quality equipment at the lowest prices isn’t enough. We strive to exceed your expectations by providing the highest level of service from start to finish—no sales talk or runaround.</p>
  <ul class="ticks">
    <li><svg width="13" height="13" viewBox="0 0 13 13"><circle cx="6.5" cy="6.5" r="6.5" fill="#0677BA"/><path d="M3.5 6.7l2 2 4-4" fill="none" stroke="#fff" stroke-width="1.5"/></svg>We buy huge packages of equipment, 100+ at a time, so we get a great price on what we buy.</li>
    <li><svg width="13" height="13" viewBox="0 0 13 13"><circle cx="6.5" cy="6.5" r="6.5" fill="#0677BA"/><path d="M3.5 6.7l2 2 4-4" fill="none" stroke="#fff" stroke-width="1.5"/></svg>We don’t operate a big retail sales lot, so we don’t have all that overhead cost.</li>
    <li><svg width="13" height="13" viewBox="0 0 13 13"><circle cx="6.5" cy="6.5" r="6.5" fill="#0677BA"/><path d="M3.5 6.7l2 2 4-4" fill="none" stroke="#fff" stroke-width="1.5"/></svg>We sell at a lower profit margin, and make it up by selling a lot more equipment.</li>
  </ul>
</section>

<!-- BLOG -->
<section class="blog">
  <div class="abs" style="left:0;width:1200px;top:3340px;text-align:center;font-size:15px;font-weight:500">
    <span style="border-left:4px solid var(--blue);padding:0 10px">Learn Smarter, Grow Faster</span><span style="border-left:4px solid var(--blue)"></span>
  </div>
  <h2 class="h2" style="left:0;width:1200px;top:3364px;text-align:center">Latest Blog From Brelvon</h2>
  <a class="btn" style="left:509px;top:3431px;width:182px;height:45px">View More Blog</a>

  <div class="blog-img" style="left:170px;background:linear-gradient(180deg,#707780,#c9cdd1 50%,#8d8a82)" role="img" aria-label="Close-up of an auxiliary power unit on a truck"></div>
  <div class="blog-meta" style="left:170px"><div class="date">JULY 26, 2025</div><h4>Transform Your Trucking Experience With an APU!</h4><p>Long hauls can be tough, especially when it comes to finding...</p></div>

  <div class="blog-img" style="left:463px;background:linear-gradient(180deg,#9fb9d6,#d8dde2 35%,#3b4048 70%,#9a9ea3)" role="img" aria-label="Front grille of a white semi truck"></div>
  <div class="blog-meta" style="left:463px"><div class="date">JULY 26, 2025</div><h4>Why Haulmark Ridgeline’s are the Better Choice</h4><p>When it comes to choosing the right truck for your hauling needs, the decision...</p></div>

  <div class="blog-img" style="left:756px;background:linear-gradient(180deg,#7aaee0,#b8d2ec 35%,#4f6b48 55%,#c7cdd2 75%,#8f9498)" role="img" aria-label="Large lot full of parked trucks and trailers"></div>
  <div class="blog-meta" style="left:756px"><div class="date">JULY 26, 2025</div><h4>Save Big: Learn to Buy Trucks Wholesale</h4><p>If so, work with a wholesale truck dealer like Brelvon! Wholesale dealers specialize...</p></div>
</section>

<!-- CTA -->
<section class="cta">
  <div class="abs cta-bg" role="img" aria-label="Blue semi truck parked at a loading dock with trailers"></div>
  <div class="abs" style="left:650px;top:3935px;width:550px;height:368px;background:linear-gradient(90deg,rgba(20,26,34,0) 0%,rgba(20,26,34,.45) 40%)"></div>
  <div class="eyebrow" style="left:662px;top:3986px;color:#fff">How Can We Help?</div>
  <h2 class="h2" style="left:660px;top:4008px;color:#fff;line-height:49px">Have More<br>Equipment Than<br>You Need?</h2>
  <p class="abs" style="left:662px;top:4166px;font-size:13.5px;color:#fff">Turn idle assets into working capital—fast, secure, and hassle-free.</p>
  <a class="btn" style="left:660px;top:4203px;width:181px;height:45px">Sell Your Equipment</a>
</section>

<!-- FOOTER -->
<footer>
  <div class="abs footer-bg"></div>
  <div class="abs" style="left:170px;top:4356px">
    <div class="logo-name" style="font-size:34px;letter-spacing:1px">BRELVON</div>
    <div class="logo-name" style="font-size:19px;margin-top:2px">Truck &amp; Trailer</div>
  </div>
  <div class="foot-col" style="left:389px"><h5>Quick Links</h5><a>Sleepers</a><a>Reefers</a><a>Dry Vans</a><a>Cranes</a><a>Resources</a></div>
  <div class="foot-col" style="left:586px"><h5>Company</h5><a>About</a><a>Contact Us</a><a>Emergency Response Guide</a><a>Careers</a></div>
  <div class="foot-col" style="left:889px"><h5>Contact Us</h5><a>Phone: 555-014-2290</a><a>Email: info@brelvon.com</a></div>
  <span class="social" style="left:889px"></span>
  <span class="social" style="left:933px"></span>
  <span class="social" style="left:977px"></span>
  <div class="abs" style="left:170px;top:4522px;width:856px;height:1px;background:#dde3ea"></div>
  <p class="legal" style="left:170px">© copyright 2026 Brelvon. All Rights Reserved.</p>
  <p class="legal" style="left:745px;display:flex;gap:22px"><span>Privacy Policy</span><span>Cookies</span><span>Terms &amp; Conditions</span></p>
</footer>

</body>
</html>
```